依頼詳細
最近、全国高校用教科書を編集しています。この度、これに対応した『テキスト』を関連編集しています。全部で16 unitありますが、設問のパターンはほとんど同じものです。ですから、『unit1』を対象に、6ページの基本編集レイアウトの作成を依頼したいのです。よろしくお願いします。
記載項目
『unit1』の原稿は添付いたします。
希望イメージ
シンプル 複雑
単色 カラフル
暗い 明るい
日常 高級
遊び心 厳粛
未来的 伝統的
女性的 男性的
希望する色
納品ファイル
• 高解像度JPG (.jpg)
• イラストレーター形式 (.ai)
補足説明
■ 選んだ理由

全ページのバランスが最もとれており、見本ページにふさわしかったので、本提案を当選として選びました。

■ 提案者全員のお礼・コメント

お盆休みの中、たくさんの御提案をいただきまして、大変感謝しております。当社は出版社ですから、依頼事項が続きます。今後とも、よろしくお願い申し上げます。

```html
<!DOCTYPE html>
<html lang="ja">
<head>
<meta charset="UTF-8">
<title>Unit 1 Vocabulary (Basic)</title>
<link href="https://fonts.googleapis.com/css2?family=Noto+Sans+JP:wght@400;500;700&family=Noto+Serif+JP:wght@400;600&display=swap" rel="stylesheet">
<style>
  :root{
    --ink:#1a1a1a;
    --rule:#333333;
    --soft:#d9d9d9;
    --tab:#2b2b2b;
    --paper:#ffffff;
  }
  *{box-sizing:border-box;margin:0;padding:0;}
  html,body{width:846px;height:1200px;overflow:hidden;background:var(--paper);}
  body{font-family:"Noto Serif JP",serif;color:var(--ink);font-size:13px;}
  .sheet{position:relative;width:846px;height:1200px;padding:38px 62px 0 62px;}

  .page-head{display:flex;align-items:flex-end;border-bottom:1.5px solid var(--rule);padding-bottom:4px;}
  .unit-tab{background:var(--tab);color:#fff;font-family:"Noto Sans JP",sans-serif;font-weight:700;font-size:11px;padding:3px 10px;letter-spacing:.05em;}
  .lesson-title{font-family:"Noto Sans JP",sans-serif;font-weight:700;font-size:16px;margin-left:14px;flex:1;}
  .book-title{font-family:"Noto Sans JP",sans-serif;font-size:10px;}

  .title-bar{display:flex;border:1.5px solid var(--rule);margin-top:10px;height:36px;align-items:stretch;}
  .title-bar .name{flex:1;font-family:"Noto Sans JP",sans-serif;font-weight:700;font-size:16px;display:flex;align-items:center;padding-left:10px;border-right:1px solid var(--rule);}
  .title-bar .field{width:190px;border-right:1px solid var(--rule);font-family:"Noto Sans JP",sans-serif;font-size:10px;padding:4px 6px;}
  .title-bar .grade{width:120px;font-family:"Noto Sans JP",sans-serif;font-size:10px;display:flex;align-items:center;padding-left:6px;gap:10px;}
  .title-bar .grade b{font-size:15px;font-weight:500;letter-spacing:.3em;}

  .task{display:flex;margin-top:16px;}
  .task-no{width:28px;height:28px;border:1.5px solid var(--rule);font-family:"Noto Sans JP",sans-serif;font-weight:700;font-size:15px;display:flex;align-items:center;justify-content:center;flex:none;margin-right:16px;}
  .task-body{flex:1;}
  .instruction{font-size:12.5px;line-height:1.7;margin-bottom:4px;}
  .item{display:flex;line-height:26px;font-size:13px;}
  .item .n{width:22px;flex:none;}
  .item .en{width:250px;}
  .item .paren{width:230px;}
  .item .br{width:68px;}
  .choice .en{width:auto;}
  .pair{margin-bottom:8px;}
  .pair .ja{line-height:24px;}
  .pair .en{line-height:24px;padding-left:22px;}
  .rearrange{margin-bottom:6px;}
  .rearrange .ja{line-height:24px;}
  .answer-line{margin:18px 0 6px 22px;border-bottom:1px solid var(--rule);height:1px;}
</style>
</head>
<body>
<div class="sheet">
  <header class="page-head">
    <span class="unit-tab">UNIT 1</span>
    <span class="lesson-title">Oliver, This Is Milo</span>
    <span class="book-title">Milo Small</span>
  </header>

  <div class="title-bar">
    <div class="name">Vocabulary (Basic)</div>
    <div class="field">名前</div>
    <div class="grade">評価 <b>ABC</b></div>
  </div>

  <section class="task">
    <div class="task-no">1</div>
    <div class="task-body">
      <p class="instruction">次の各文を日本語に訳し，SV, SVC, SVO, SVOO, SVOC のどの文型か答え，[　]に記入しなさい。</p>
      <div class="item"><span class="n">①</span><span class="en">She smelled the lilies.</span><span class="paren">(　　　　　　　　　　　　　)</span><span class="br">[　　]</span><span class="br">[　　]</span></div>
      <div class="item"><span class="n">②</span><span class="en">John showed his diary to his wife.</span><span class="paren">(　　　　　　　　　　　　　)</span><span class="br">[　　]</span><span class="br">[　　]</span></div>
      <div class="item"><span class="n">③</span><span class="en">Mary bought her mother a rose.</span><span class="paren">(　　　　　　　　　　　　　)</span><span class="br">[　　]</span><span class="br">[　　]</span></div>
      <div class="item"><span class="n">④</span><span class="en">She left the door open.</span><span class="paren">(　　　　　　　　　　　　　)</span><span class="br">[　　]</span><span class="br">[　　]</span></div>
      <div class="item"><span class="n">⑤</span><span class="en">John lives in Tokyo.</span><span class="paren">(　　　　　　　　　　　　　)</span><span class="br">[　　]</span><span class="br">[　　]</span></div>
      <div class="item"><span class="n">⑥</span><span class="en">That sounds like a great idea.</span><span class="paren">(　　　　　　　　　　　　　)</span><span class="br">[　　]</span><span class="br">[　　]</span></div>
    </div>
  </section>

  <section class="task">
    <div class="task-no">2</div>
    <div class="task-body">
      <p class="instruction">(　　)内から適切な語句を選びなさい。</p>
      <div class="item choice"><span class="n">①</span><span class="en">I totally ( agree / agree with / agree in ) you.</span></div>
      <div class="item choice"><span class="n">②</span><span class="en">Have you ( heard / heard from / heard with ) John lately?</span></div>
      <div class="item choice"><span class="n">③</span><span class="en">He ( looked / looked at / looked on ) me.</span></div>
      <div class="item choice"><span class="n">④</span><span class="en">His remark ( left / made / did ) me angry.</span></div>
    </div>
  </section>

  <section class="task">
    <div class="task-no">3</div>
    <div class="task-body">
      <p class="instruction">日本語に合うように，(　　　)に適切な語を入れなさい。</p>
      <div class="pair"><div class="ja">①　先生は私たちのことをよく面倒をみてくれる。</div><div class="en">Our teacher looks (　　　　　　) us well.</div></div>
      <div class="pair"><div class="ja">②　私たちは試合に勝つのは難しいとわかった。</div><div class="en">We (　　　　　　) it difficult to (　　　　　　) the game.</div></div>
      <div class="pair"><div class="ja">③　先生はその生徒に教室を出るように言った。</div><div class="en">The teacher (　　　　　　) the student (　　　　　　) leave the classroom.</div></div>
      <div class="pair"><div class="ja">④　彼は英語を勉強するのを楽しんでいる。</div><div class="en">He (　　　　　　) studying English.</div></div>
      <div class="pair"><div class="ja">⑤　彼はパーティ会場にやっと到着した。</div><div class="en">He finally (　　　　　　) at the party place.</div></div>
    </div>
  </section>

  <section class="task">
    <div class="task-no">4</div>
    <div class="task-body">
      <p class="instruction">日本語に合うように，(　　　)内の語句を並べかえなさい。</p>
      <div class="rearrange"><div class="ja">①　彼女はパーティを楽しんだ。　She ( herself / enjoyed / the party / at ).</div><div class="answer-line"></div></div>
      <div class="rearrange"><div class="ja">②　私たちは彼のことをほっておいた。　( left / alone / him / we ).</div><div class="answer-line"></div></div>
      <div class="rearrange"><div class="ja">③　彼は私たちにそこへの行き方を教えてくれた。　He ( to / how / us / showed / there / get ).</div><div class="answer-line"></div></div>
      <div class="rearrange"><div class="ja">④　皆，最初は少し緊張しているように見えた。　Everybody ( at first / nervous / a little / looked ).</div><div class="answer-line"></div></div>
      <div class="rearrange"><div class="ja">⑤　近所で大きな火事が発生した。　There ( a / fire / neighborhood / big / was / in / the ).</div><div class="answer-line"></div></div>
    </div>
  </section>
</div>
</body>
</html>
```